Website Redesign - We Need Your Magic!

Hello we are looking for you to help us re-design a high end and professional website for a high-end private school.

Here is the current site: http://www.veltrasham.example/

NOTE THIS IS DESIGN ONLY, NO CODING :)

The image they want to portray is that of high quality sports and education, in a creative "un-stiff" way.

Menu Bar: Horizontal

Look and Feel:

Site Colors: Dark green and a Gold yellow (logos are attached)

This site will represent a school so the look must be clean, bold, and classy. The site must have a very clean user interface, with things easily recognizable. Think simple.

The site should be visually appealing! If you come to me with templates, or a ton of text you will be out.

This site should be outside the box, we do not want boring, we do not want status quo. This site should instill excitement, innovation, and athletics.

So the main points again are:

1. High-end and classy look, with creative feel
2. Simple and clear navigation style
3. To cover the Junior and High School - Veltrasham College Schools

Think outside the box. We look forward to seeing what you come up with!!

Thank you for helping us create an amazing site for the school!

Industry/Entity Type

School

```html
<!DOCTYPE html>
<html lang="en">
<head>
<meta charset="utf-8">
<title>Veltrasham College</title>
<link rel="stylesheet" href="https://fonts.googleapis.com/css2?family=Roboto+Condensed:wght@400;500;700&family=Open+Sans:wght@400;600&family=Raleway:wght@400;500&display=swap">
<style>
:root{
  --green:#1a6b35;
  --green-dark:#155a2c;
  --yellow:#f5e82a;
  --ink:#3b3b3b;
  --muted:#8a8a8a;
  --panel:#f1efe9;
  --white:#ffffff;
}
*{margin:0;padding:0;box-sizing:border-box}
html,body{width:770px;height:1200px;overflow:hidden;background:var(--white)}
body{position:relative;font-family:'Open Sans',sans-serif;color:var(--ink)}
.abs{position:absolute}

/* header */
.header-band{left:0;top:0;width:770px;height:76px;background:var(--green)}
.nav-band{left:0;top:76px;width:770px;height:36px;background:var(--yellow);border-bottom:1px solid #d9c900}
.crest-tab{left:308px;top:76px;width:154px;height:62px;background:var(--green);border-radius:0 0 40px 40px;border:2px solid var(--yellow);border-top:none}
.crest{left:308px;top:14px;width:154px;height:112px;display:flex;flex-direction:column;align-items:center;justify-content:flex-end;gap:10px}
.crest-dot{width:52px;height:52px;border-radius:50%;background:var(--yellow)}
.crest-name{font-family:'Roboto Condensed',sans-serif;font-weight:700;font-size:13px;color:var(--yellow);letter-spacing:1.5px}
.social{left:70px;top:28px;display:flex;gap:4px}
.search{left:510px;top:26px;width:188px;height:26px;border:1px solid var(--yellow);display:flex}
.search span{flex:1;font-size:8px;color:#7fae8b;padding:7px 6px;font-style:italic}
.search b{width:26px;background:var(--yellow);display:flex;align-items:center;justify-content:center}
.nav{top:88px;font-family:'Roboto Condensed',sans-serif;font-weight:400;font-size:11.5px;color:#1f3d22;display:flex;gap:18px}
.nav .active{color:var(--green)}

/* slider */
.slider-bg{left:0;top:112px;width:770px;height:282px;background:linear-gradient(90deg,#e9c7c2 0%,#f3ecea 8%,#fff 12%,#fff 88%,#eef2ee 94%,#dfe7df 100%)}
.slide{left:72px;top:112px;width:626px;height:272px;border:2px solid var(--green);border-top:none;background:linear-gradient(160deg,#d8cfae 0%,#b9a987 45%,#6f7b4a 75%,#4d5e32 100%)}
.caption{left:74px;top:333px;width:622px;height:49px;background:rgba(20,20,20,.72);padding:8px 10px;color:#fff}
.caption h2{font-family:'Raleway',sans-serif;font-weight:400;font-size:13px}
.caption p{font-size:7.8px;font-weight:600;margin-top:5px}
.arrow{width:29px;height:29px}

/* welcome */
.welcome-title{left:70px;top:402px;font-family:'Roboto Condensed',sans-serif;font-weight:400;font-size:15.5px;color:#777}
.welcome-title em{font-style:normal;color:var(--green)}
.welcome-rule{left:70px;top:423px;width:86px;height:2px;background:#999}
.welcome-img{left:70px;top:434px;width:214px;height:116px;background:linear-gradient(135deg,#3d5a2a 0%,#5d6b3a 40%,#9b9a7a 75%,#c8bfa8 100%)}
.welcome-copy{left:302px;top:430px;width:396px;font-size:8.8px;line-height:15px;color:#444}
.welcome-copy p+p{margin-top:5px}

/* columns */
.tab{height:32px;width:140px;font-family:'Roboto Condensed',sans-serif;font-weight:400;font-size:14px;padding:7px 9px}
.tab-yellow{left:70px;top:576px;background:linear-gradient(100deg,var(--yellow) 82%,#e0d300 82%);color:var(--green)}
.tab-green{left:246px;top:576px;background:linear-gradient(100deg,var(--green) 82%,var(--green-dark) 82%);color:var(--yellow)}
.col-intro{top:616px;width:150px;font-size:10px;line-height:14.5px;color:var(--muted)}
.ticks{top:654px;list-style:none;font-size:8.2px;color:var(--ink)}
.ticks li{height:27px;display:flex;gap:10px;align-items:flex-start}
.ticks li.lead{color:var(--green);font-weight:600}
.news{left:416px;top:576px;width:282px;height:168px;background:var(--panel);padding:9px 12px}
.news h3{font-family:'Roboto Condensed',sans-serif;font-weight:400;font-size:14.5px;color:var(--green)}
.news-item{display:flex;gap:18px;font-size:7.8px;line-height:12.5px;padding:8px 0 10px;width:242px;border-bottom:1px solid #ddd}
.news-item:last-child{border-bottom:none}
.news-item b{color:var(--green);font-weight:600;width:30px;flex:none}
.news-item.lead span{color:var(--green)}
.news-scroll{left:684px;top:610px;width:3px;height:28px;background:#bbb}

/* events */
.events{left:70px;top:776px;width:346px;height:200px;background:var(--panel);border-top:2px solid var(--green);padding:8px 12px}
.events h3{font-family:'Roboto Condensed',sans-serif;font-weight:400;font-size:14px;color:var(--green)}
.event{display:flex;gap:12px;align-items:flex-start;margin-top:14px}
.date{width:35px;height:38px;background:#e3e3e3;border-top:14px solid var(--green);position:relative;font-family:'Roboto Condensed',sans-serif;text-align:center;flex:none}
.date i{position:absolute;top:-13px;left:0;width:100%;font-size:8px;color:#fff}
.date b{font-size:12px;color:var(--green);line-height:22px}
.event p{font-size:9.6px;line-height:16.5px;color:#666;width:250px}
.event.lead p{color:var(--green)}
.events-photo{left:416px;top:778px;width:282px;height:198px;background:linear-gradient(180deg,#4d5a3c 0%,#30452f 40%,#1f3524 70%,#7a5e3a 100%)}
.events-caption{left:416px;top:945px;width:282px;height:31px;background:rgba(10,10,10,.7);display:flex;align-items:center;justify-content:space-between;padding:0 12px}
.events-caption span{font-family:'Roboto Condensed',sans-serif;font-size:13.5px;color:var(--yellow)}

/* partners */
.partners{left:70px;top:1008px;width:628px;height:44px;display:flex;justify-content:space-around;align-items:center}
.partner{display:flex;align-items:center;gap:6px;font-weight:600;font-size:15px;color:#444}
.partner i{width:14px;height:14px;background:#e08a1e;display:block}

/* footer */
.footer{left:0;top:1076px;width:770px;height:76px;background:var(--green);border-bottom:2px solid var(--yellow)}
.footer-links{left:70px;top:1088px;font-size:8px;color:#cfe0c5}
.footer-links a{color:inherit;text-decoration:none}
.footer-links .sep{margin:0 6px}
.footer-links .active{color:var(--yellow)}
.footer-line{left:70px;font-size:8px;color:#e7efe3}
.footer-line b{color:var(--yellow);font-weight:600}
.footer-tab{left:570px;top:1070px;width:126px;height:122px;background:var(--green);border:2px solid var(--yellow);border-top:none;border-radius:0 0 34px 34px;display:flex;flex-direction:column;align-items:center;justify-content:center;gap:8px}
.footer-tab .crest-dot{width:40px;height:40px}
.footer-tab .crest-name{font-size:11px}
.copyright{left:366px;top:1162px;font-size:8px;color:var(--green)}
</style>
</head>
<body>

<div class="abs header-band"></div>
<div class="abs nav-band"></div>
<div class="abs crest-tab"></div>
<div class="abs crest"><span class="crest-dot"></span><span class="crest-name">VELTRASHAM</span></div>

<div class="abs social" aria-label="Social links">
  <svg width="154" height="22" viewBox="0 0 154 22">
    <polygon points="0,0 22,0 11,22" fill="#f5e82a"/>
    <polygon points="14,22 36,22 25,0" fill="#4fa35f"/>
    <polygon points="32,0 54,0 43,22" fill="#4fa35f"/>
    <polygon points="46,22 68,22 57,0" fill="#4fa35f"/>
    <polygon points="64,0 86,0 75,22" fill="#4fa35f"/>
    <polygon points="78,22 100,22 89,0" fill="#4fa35f"/>
    <polygon points="96,0 118,0 107,22" fill="#4fa35f"/>
    <polygon points="110,22 132,22 121,0" fill="#4fa35f"/>
  </svg>
</div>

<div class="abs search"><span>Search</span><b>
  <svg width="12" height="12" viewBox="0 0 12 12"><circle cx="7" cy="5" r="3.5" fill="none" stroke="#1a6b35" stroke-width="1.5"/><line x1="4.5" y1="7.5" x2="1" y2="11" stroke="#1a6b35" stroke-width="1.8"/></svg>
</b></div>

<nav class="abs nav" style="left:70px"><span class="active">HOME</span><span>ABOUT US</span><span>ACADEMICS</span><span>SPORTS</span></nav>
<nav class="abs nav" style="left:483px"><span>JOINING</span><span>COLLEGE WORK</span><span>CONTACT US</span></nav>

<div class="abs slider-bg" role="img" aria-label="Faded photo of pupils playing sport behind the slider"></div>
<div class="abs slide" role="img" aria-label="Photo of the college building with palm trees"></div>
<div class="abs caption">
  <h2>Lorem ipsum dolor sit amet consectetur adipiscing elit</h2>
  <p>Proin ornare augue purus, eu cursus nibh vestibulum quis. Sed id nisi eget odio consectetur imperdiet.</p>
</div>
<svg class="abs arrow" style="left:29px;top:235px" viewBox="0 0 29 29"><circle cx="14.5" cy="14.5" r="13.5" fill="#fff" stroke="#222" stroke-width="1.5"/><polyline points="16.5,8.5 10.5,14.5 16.5,20.5" fill="none" stroke="#222" stroke-width="2.5"/></svg>
<svg class="abs arrow" style="left:711px;top:231px" viewBox="0 0 29 29"><circle cx="14.5" cy="14.5" r="13.5" fill="#fff" stroke="#1a6b35" stroke-width="1.5"/><polyline points="12.5,8.5 18.5,14.5 12.5,20.5" fill="none" stroke="#1a6b35" stroke-width="2.5"/></svg>

<h1 class="abs welcome-title">WELCOME TO <em>VELTRASHAM</em></h1>
<div class="abs welcome-rule"></div>
<svg class="abs" style="left:686px;top:404px" width="13" height="13" viewBox="0 0 13 13"><circle cx="6.5" cy="6.5" r="6.5" fill="#1a6b35"/><polygon points="5,3.5 9.5,6.5 5,9.5" fill="#fff"/></svg>
<div class="abs welcome-img" role="img" aria-label="Photo of the college bus"></div>
<div class="abs welcome-copy">
  <p>Lorem ipsum dolor sit amet, consectetur adipiscing elit. Proin eu accumsan justo. Nullam luctus sapien vitae mauris aliquet, et convallis dui fermentum. Integer non dolor ultricies, vehicula erat eu, sagittis leo. In porta vitae nisi vel malesuada. Nunc non ultrices velit. Nunc iaculis dolor vulpu­tate, gravida augue vitae, interdum arcu.</p>
  <p>Integer non urna consequat, sagittis ante ac, varius mi. Pellentesque convallis mi ac mauris hen­drerit pellentesque. Aliquam egestas at velit eu mattis. Sed et facilisis mauris, vitae vestibulum lorem. Praesent iaculis, quam et rutrum hendrerit, odio dolor pretium justo, ac eleifend urna mauris aliquet velit. Nullam laoreet sollicitudin orci, id tincidunt turpis mollis eget.</p>
</div>

<div class="abs tab tab-yellow">ACADEMICS</div>
<div class="abs tab tab-green">STUDENTS LIFE</div>
<p class="abs col-intro" style="left:70px">Lorem ipsum sit consectetuer apiscing elit sed diam</p>
<p class="abs col-intro" style="left:246px">Lorem ipsum sit consectetuer apiscing elit sed diam</p>

<ul class="abs ticks" style="left:70px">
  <li class="lead"><svg width="8" height="8" viewBox="0 0 8 8"><polyline points="1,4 3,6.5 7,1.5" fill="none" stroke="#1a6b35" stroke-width="1.5"/></svg>Undergraduate Education</li>
  <li><svg width="8" height="8" viewBox="0 0 8 8"><polyline points="1,4 3,6.5 7,1.5" fill="none" stroke="#1a6b35" stroke-width="1.5"/></svg>Colleges &amp; Departments</li>
  <li><svg width="8" height="8" viewBox="0 0 8 8"><polyline points="1,4 3,6.5 7,1.5" fill="none" stroke="#1a6b35" stroke-width="1.5"/></svg>Graduate School</li>
  <li><svg width="8" height="8" viewBox="0 0 8 8"><polyline points="1,4 3,6.5 7,1.5" fill="none" stroke="#1a6b35" stroke-width="1.5"/></svg>Distance Learning</li>
</ul>
<ul class="abs ticks" style="left:246px">
  <li class="lead"><svg width="8" height="8" viewBox="0 0 8 8"><polyline points="1,4 3,6.5 7,1.5" fill="none" stroke="#1a6b35" stroke-width="1.5"/></svg>Clubs &amp; Organizations</li>
  <li><svg width="8" height="8" viewBox="0 0 8 8"><polyline points="1,4 3,6.5 7,1.5" fill="none" stroke="#1a6b35" stroke-width="1.5"/></svg>Living On and Off Campus</li>
  <li><svg width="8" height="8" viewBox="0 0 8 8"><polyline points="1,4 3,6.5 7,1.5" fill="none" stroke="#1a6b35" stroke-width="1.5"/></svg>Recreational Sports</li>
  <li><svg width="8" height="8" viewBox="0 0 8 8"><polyline points="1,4 3,6.5 7,1.5" fill="none" stroke="#1a6b35" stroke-width="1.5"/></svg>Photo Galleries</li>
</ul>

<section class="abs news">
  <h3>LATEST NEWS</h3>
  <div class="news-item lead"><b>Mar. 24</b><span>Lorem ipsum dolor sit amet, consectetuer adipiscing elit, sed diam nonummy nibh euismod.</span></div>
  <div class="news-item"><b>Mar. 24</b><span>Tincidunt ut laoreet dolore magna aliquam erat volutpat. Ut wisi enim ad minim veniam.</span></div>
  <div class="news-item"><b>Mar. 24</b><span>Quis nostrud exerci tation ullamcorper suscipit lobortis nisl ut aliquip ex ea commodo consequat.</span></div>
</section>
<div class="abs news-scroll"></div>

<section class="abs events">
  <h3>UPCOMING EVENTS</h3>
  <div class="event lead"><div class="date"><i>JUL</i><b>04</b></div><p>Lorem ipsum dolor sit amet, consectetuer adipiscing elit, sed diam nonummy nibh euismod.</p></div>
  <div class="event"><div class="date"><i>JUL</i><b>04</b></div><p>Lorem ipsum dolor sit amet, consectetuer adipiscing elit, sed diam nonummy nibh euismod.</p></div>
  <div class="event"><div class="date"><i>JUL</i><b>04</b></div><p>Lorem ipsum dolor sit amet, consectetuer adipiscing elit, sed diam nonummy nibh euismod.</p></div>
</section>
<div class="abs events-photo" role="img" aria-label="Group photo of pupils in school uniform"></div>
<div class="abs events-caption"><span>NATIONAL COACHING CONFERENCE</span>
  <svg width="13" height="13" viewBox="0 0 13 13"><circle cx="6.5" cy="6.5" r="6.5" fill="#f5e82a"/><polygon points="5,3.5 9.5,6.5 5,9.5" fill="#1a1a1a"/></svg>
</div>

<div class="abs partners">
  <span class="partner" style="color:#1d3f9a">Northgate</span>
  <span class="partner"><i></i>Listwise</span>
  <span class="partner"><i></i>Hallo!</span>
  <span class="partner"><i style="border-radius:50%"></i>Brightline</span>
</div>

<div class="abs footer"></div>
<div class="abs footer-links"><a class="active">Home</a><span class="sep">/</span><a>About Us</a><span class="sep">/</span><a>Academics</a><span class="sep">/</span><a>Sports Joining</a><span class="sep">/</span><a>College Work</a><span class="sep">/</span><a>Contact Us</a></div>
<div class="abs footer-line" style="top:1107px"><b>Add:</b> Veltrasham College, Mill Road, water tower take the 1st Right turn.</div>
<div class="abs footer-line" style="top:1126px"><b>Call:</b> 0700 000 111 &nbsp;/&nbsp; 0700 000 222<span style="margin-left:28px"><b>Email:</b> admin@veltrasham.example</span></div>
<div class="abs footer-tab"><span class="crest-dot"></span><span class="crest-name">VELTRASHAM</span></div>
<div class="abs copyright">Copyright © 2014 Veltrasham. All Rights Reserved.</div>

</body>
</html>
```